RTW Business Card Design

We are an independent auto dealer who specializes in commercial & fleet vehicles, we are family owned and operated and have been in business since 2001. We stock late model, low mileage, white trucks & vans. We mostly deal with companies in the construction and service industries. We are just looking to try to freshen up our old business card, we do not want to change the logo at this point, because it is well know within the southwest region & construction community. I have attached our logo and a PDF of our current business card for reference.
Updates
If the address is stacked there is no comma (,) after NE. Everyone keeps putting it in with this format and it is not correct.
842 Ventana Blvd NE
Albuquerque, NM 87120
If the address is all on one line, then there will be a comma (,) after NE
842 Ventana Blvd NE, Albuquerque, NM 87120
Please make changes accordingly, thank you for your attention in this matter.
Industry/Entity Type
Construction
Contact Information for Business Card
842 Ventana Blvd NE, Albuquerque, NM 87120, Marcus Delaney, Vice President, marcus@rtwvehicledepot.com, www.RTWvehicledepot.com, ph 505-610-2247, fax 505-472-8156, cell 505-238-6094
Look and feel
Each slider illustrates characteristics of the customer's brand and the style your logo design should communicate.

```html
<!DOCTYPE html>
<html lang="en">
<head>
<meta charset="utf-8">
<title>RTW Auto Sales – Business Card</title>
<link rel="stylesheet" href="https://fonts.googleapis.com/css2?family=Arimo:wght@400;700&display=swap">
<style>
  :root {
    --backdrop: #1d1d1d;
    --card: #ffffff;
    --ink: #111111;
    --accent: #e3202a;
    --icon-bg: #f07b7b;
    --icon-ink: #3a1212;
  }
  * { box-sizing: border-box; margin: 0; padding: 0; }
  html, body {
    width: 1200px; height: 1000px; overflow: hidden;
    background: var(--backdrop);
    font-family: "Arimo", Arial, sans-serif;
    color: var(--ink);
  }
  .business-card {
    position: absolute; left: 75px; top: 200px;
    width: 1050px; height: 600px;
    background: var(--card);
    box-shadow: 0 10px 30px rgba(0,0,0,.5);
  }
  .brand-name {
    position: absolute; left: 110px; top: 200px;
    font-size: 58px; font-weight: 700; letter-spacing: 1px;
    color: var(--ink); white-space: nowrap;
  }
  .address {
    position: absolute; left: 120px; top: 330px;
    font-size: 30px; line-height: 38px;
  }
  .contact {
    position: absolute; right: 110px; top: 95px;
    text-align: right;
  }
  .person-name { font-size: 30px; font-weight: 700; }
  .person-title { font-size: 26px; margin-top: 4px; }
  .phone-list { list-style: none; margin-top: 34px; margin-right: 30px; }
  .phone-list li {
    display: flex; align-items: center; justify-content: flex-end;
    font-size: 27px; height: 40px;
  }
  .phone-icon {
    width: 30px; height: 30px; margin-right: 14px;
  }
  .email, .website { font-size: 26px; }
  .email { margin-top: 42px; }
  .website { margin-top: 4px; }
  .website .domain { color: var(--accent); }
</style>
</head>
<body>
  <div class="business-card">
    <div class="brand-name">RTW AUTO SALES</div>

    <div class="address">
      842 Ventana Blvd NE<br>
      Albuquerque, NM 87120
    </div>

    <div class="contact">
      <div class="person-name">Marcus Delaney</div>
      <div class="person-title">Vice President</div>

      <ul class="phone-list">
        <li>
          <svg class="phone-icon" viewBox="0 0 30 30" aria-label="Cell">
            <circle cx="15" cy="15" r="15" fill="var(--icon-bg)"/>
            <rect x="10.5" y="7" width="9" height="16" rx="1.5" fill="none" stroke="var(--icon-ink)" stroke-width="1.8"/>
            <line x1="13" y1="20" x2="17" y2="20" stroke="var(--icon-ink)" stroke-width="1.5"/>
          </svg>
          505-238-6094
        </li>
        <li>
          <svg class="phone-icon" viewBox="0 0 30 30" aria-label="Phone">
            <circle cx="15" cy="15" r="15" fill="var(--icon-bg)"/>
            <rect x="8" y="13" width="14" height="9" rx="1.5" fill="none" stroke="var(--icon-ink)" stroke-width="1.8"/>
            <path d="M8 12 Q15 6 22 12" fill="none" stroke="var(--icon-ink)" stroke-width="2"/>
            <circle cx="15" cy="17.5" r="2" fill="var(--icon-ink)"/>
          </svg>
          505-610-2247
        </li>
        <li>
          <svg class="phone-icon" viewBox="0 0 30 30" aria-label="Fax">
            <circle cx="15" cy="15" r="15" fill="var(--icon-bg)"/>
            <path d="M10 8 L13 8 L14 12 L12 13.5 Q13.5 17 16.5 18.5 L18 16.5 L22 17.5 L22 20.5 Q16 22 11.5 17.5 Q8 13 10 8 Z" fill="var(--icon-ink)"/>
          </svg>
          505-472-8156
        </li>
      </ul>

      <div class="email">marcus@rtwvehicledepot.com</div>
      <div class="website">www.<span class="domain">RTWvehicledepot</span>.com</div>
    </div>
  </div>
</body>
</html>
```